Poster for a Vegetarian Food Truck/Restaurant

Ours is a food truck with lots of greens in the menu. The name of our restaurant is Plum Nibbles.

I want to create a Poster image for the restaurant. Please submit designs on any one or both the themes described below

Size: 1.6 meters by 4.6 meters (horizontal)

Design Theme #1
A poster based off 'Newspaper front page'.
The poster should look like the front page of a newspaper with 'Plum Nibbles' as its name. The Plum Nibbles should appear prominently (in green color, possibly light green or lemon color). The poster will have a few snippets about benefits of certain food items or some trivia along with an image. For example 'Garlic is high in minerals & vitamins', 'Chickpeas are high on fiber'. I'll decide on the exact text meanwhile.

I have attached 2 sample images to give an idea.

Design Theme #2

It should consist of the following 3 components:
1. Green Forest like back ground
2. Image of a chef with a welcoming, smiling face
3. The text 'Plum Nibbles' should appear in the poster

I want Tobin Marsh lookalike, the main character from the animation movie 'Sunny Days over Dumpling Hill' to be the chef placed in the poster.
The chef should appear confident, smiling, young with his typical hair style

A sample picture of tobin marsh is attached in the brief

Target Market(s)

The poster will be pasted on a food truck

Industry/Entity Type

Restaurant

Requirements
Must have
• Poster with light but high resolution image(s)
• Attention to detail
Should not have
• The poster should not have dense/dark colors

```html
<!DOCTYPE html>
<html lang="en">
<head>
<meta charset="utf-8">
<title>Plum Nibbles – Front Page Poster</title>
<link href="https://fonts.googleapis.com/css2?family=Poiret+One&family=Questrial&display=swap" rel="stylesheet">
<style>
  :root {
    --leaf: #9bbd0f;
    --lemon: #dfdc00;
    --leaf-pale: #dfe9c6;
    --paper: #f2f2f2;
    --card: #ffffff;
    --rule: #9a9a9a;
    --photo: #8a8a8a;
    --ink: #6f6f6f;
    --ink-soft: #7c7c7c;
  }
  * { margin: 0; padding: 0; box-sizing: border-box; }
  html, body { width: 1200px; height: 1200px; overflow: hidden; background: #fff; }
  .stage { position: relative; width: 1200px; height: 1200px; }

  .poster {
    position: absolute; left: 46px; top: 344px;
    width: 1381px; height: 470px;
    transform: scale(0.8); transform-origin: 0 0;
    background: var(--card);
  }
  .poster > * { position: absolute; }
  .shapes { left: 0; top: 0; width: 1381px; height: 470px; }

  .page { left: 86px; top: 30px; width: 1164px; height: 405px; background: var(--paper); }
  .masthead-rule { top: 30px; height: 10px; background: var(--rule); }
  .footer-rule { left: 106px; top: 412px; width: 1142px; height: 10px; background: var(--leaf); }

  .smallcaps { font-family: "Poiret One", cursive; font-variant: small-caps; font-weight: 400; color: var(--ink); }
  .body-copy { font-family: "Questrial", sans-serif; color: var(--ink-soft); white-space: nowrap; }

  .title {
    left: 116px; top: 68px; width: 180px;
    font-family: "Questrial", sans-serif; font-weight: 400;
    color: var(--ink); font-size: 44px; line-height: 52px; text-align: center;
  }
  .lead-head { left: 124px; top: 186px; font-size: 26px; line-height: 32px; }
  .lead-copy { left: 124px; top: 250px; font-size: 18px; line-height: 22.5px; }

  .photo { background: var(--photo); }
  .photo-tall { left: 300px; top: 62px; width: 178px; height: 326px; }

  .dot { width: 88px; height: 88px; border-radius: 50%; left: 506px; }
  .dot-leaf { background: var(--leaf); }
  .dot-lemon { background: var(--lemon); }
  .fact { left: 590px; width: 264px; text-align: center; font-size: 25px; line-height: 31px; font-weight: 400; }
  .divider { height: 3px; background: var(--rule); }

  .snippet-head { font-size: 20px; line-height: 22px; white-space: nowrap; }
  .snippet-copy { font-size: 13.5px; line-height: 16.3px; }
</style>
</head>
<body>
<main class="stage">
  <section class="poster" aria-label="Plum Nibbles newspaper-style poster">
    <svg class="shapes" viewBox="0 0 1381 470" aria-hidden="true">
      <polygon points="0,0 973,0 86,170" fill="var(--leaf)"/>
      <polygon points="963,30 1023,0 1083,30" fill="var(--lemon)"/>
      <polygon points="1248,205 1368,270 1248,290" fill="var(--leaf)"/>
      <polygon points="1248,118 1366,180 1248,250" fill="var(--lemon)"/>
      <polygon points="218,438 233,468 420,435" fill="var(--leaf)"/>
      <polygon points="245,436 290,452 420,436" fill="var(--lemon)"/>
    </svg>

    <div class="page"></div>
    <div class="masthead-rule" style="left:86px;width:405px"></div>
    <div class="masthead-rule" style="left:505px;width:343px"></div>
    <div class="masthead-rule" style="left:863px;width:387px"></div>

    <svg class="shapes" viewBox="0 0 1381 470" aria-hidden="true">
      <polygon points="1050,66 1078,62 1082,82 1058,86" fill="var(--leaf-pale)"/>
      <polygon points="862,182 892,180 896,198 876,208" fill="var(--leaf-pale)"/>
      <polygon points="1052,300 1080,298 1084,318 1060,322" fill="var(--leaf-pale)"/>
    </svg>

    <h1 class="title">Plum<br>Nibbles</h1>
    <h2 class="smallcaps lead-head">Lorem ips<br>&nbsp;dolor sit</h2>
    <p class="body-copy lead-copy">Lorem ipsum lor<br>sit amet, con-<br>sectetur adipi-<br>scing elit. ed a<br>cursus purus.<br>Etiam porttitor</p>

    <div class="photo photo-tall" role="img" aria-label="Photo of a fresh vegetarian dish"></div>

    <div class="dot dot-leaf" style="top:62px"></div>
    <p class="smallcaps fact" style="top:70px">Garlic is high in mine-<br>rals &amp; vitamins</p>
    <div class="divider" style="left:605px;top:164px;width:166px"></div>

    <div class="dot dot-lemon" style="top:181px"></div>
    <p class="smallcaps fact" style="top:191px">Chickpeas are high<br>on fiber</p>
    <div class="divider" style="left:608px;top:284px;width:166px"></div>

    <div class="dot dot-leaf" style="top:299px"></div>
    <p class="smallcaps fact" style="top:307px">Garlic is high in mine-<br>rals &amp; vitamins</p>

    <div class="photo" style="left:862px;top:62px;width:184px;height:91px" role="img" aria-label="Photo of garlic"></div>
    <h3 class="smallcaps snippet-head" style="left:1050px;top:65px">Lorem ipsum dolor</h3>
    <p class="body-copy snippet-copy" style="left:1054px;top:89px">Lorem ipsum dolor sit<br>amet, consectetur adipi-<br>scing elit. Donec ipsum ex,<br>mattis non placerat nec,</p>
    <div class="divider" style="left:964px;top:164px;width:166px"></div>

    <h3 class="smallcaps snippet-head" style="left:863px;top:181px">Lorem ipsum dolor</h3>
    <p class="body-copy snippet-copy" style="left:863px;top:207px">Lorem ipsum dolor sit<br>amet, consectetur adipi-<br>scing elit. Donec ipsum ex,<br>mattis non placerat nec,</p>
    <div class="photo" style="left:1048px;top:180px;width:185px;height:90px" role="img" aria-label="Photo of chickpeas"></div>
    <div class="divider" style="left:964px;top:285px;width:166px"></div>

    <div class="photo" style="left:862px;top:299px;width:184px;height:89px" role="img" aria-label="Photo of fresh greens"></div>
    <h3 class="smallcaps snippet-head" style="left:1055px;top:302px">Lorem ipsum dolor</h3>
    <p class="body-copy snippet-copy" style="left:1052px;top:326px">Lorem ipsum dolor sit<br>amet, consectetur adipi-<br>scing elit. Donec ipsum ex,<br>mattis non placerat nec,</p>

    <div class="footer-rule"></div>
  </section>
</main>
</body>
</html>
```